Flyer für Ladenlokal
Zielgruppe
Wir eröffnen zum 01.01.2024 ein Ladenlokal 'FrostaNova', welches Anwendungen zum Thema Wellness, Gesundheit, Anti Aging anbieten. Wie der Name schon sagt 'FROSTA' haben wir eine Kältekammer.
Aufgabenstellung
Ich hätte gerne auf dem Flyer die 3 Behandlungen und die Vorteile kurz erklärt:
https://www.velantor.net/de/produkte/kaeltekammern/glacix-plus/
https://vita-prisma.de/glacio-ems-anzeige/
http://www.hartung-med.de/download/HARTUNG_drainotex_D.pdf
Außerdem die Kontaktdaten und die Öffnungszeiten: (erstmal als Platzhalter)
Es sollte ein OPENING Flyer sein - vielleicht eine Opening-Rabatt-Aktion???
Das Logo ist schwarz / weiss, der Laden auch

```html
<!DOCTYPE html>
<html lang="de">
<head>
<meta charset="utf-8">
<title>FrostaNova – Große Eröffnung</title>
<link rel="stylesheet" href="https://fonts.googleapis.com/css2?family=Bebas+Neue&family=Montserrat:ital,wght@0,300;0,400;0,500;0,600;0,700;0,800;0,900;1,700;1,800;1,900&display=swap">
<style>
  :root {
    --backdrop: #8f8f8f;
    --paper: #ffffff;
    --ink: #000000;
    --heading-ink: #231f20;
    --teal: #22bed2;
    --teal-dark: #18a8bb;
    --band-shade: #0d2228;
    --hex-tint: #d9eef8;
    --muted-light: #dfe9ec;
  }
  * { box-sizing: border-box; margin: 0; padding: 0; }
  html, body { width: 1200px; height: 1117px; overflow: hidden; }
  body { background: var(--backdrop); font-family: "Montserrat", sans-serif; position: relative; }

  .flyer {
    position: absolute; left: 246px; top: 59px; width: 708px; height: 999px;
    background: var(--paper); overflow: hidden;
    box-shadow: 8px 10px 28px rgba(0,0,0,.35);
  }
  .abs { position: absolute; }

  .hex-decor {
    left: 560px; top: 0; width: 148px; height: 440px;
    background: radial-gradient(ellipse at 70% 40%, var(--hex-tint) 0%, rgba(217,238,248,.5) 45%, rgba(255,255,255,0) 80%);
  }
  .dot-grid { left: 38px; top: 50px; }

  .header-tab { left: 98px; top: 0; }
  .brand-name {
    left: 98px; top: 40px; width: 511px; text-align: center;
    color: var(--paper); font-weight: 300; font-size: 40px; letter-spacing: 6px;
  }

  .opening-date {
    left: 0; width: 708px; top: 136px; text-align: center;
    color: var(--teal); font-weight: 800; font-style: italic; font-size: 52px; letter-spacing: -1px;
  }
  .headline {
    left: 0; width: 708px; top: 186px; text-align: center;
    color: var(--heading-ink); font-weight: 900; font-style: italic; font-size: 138px; letter-spacing: -6px; line-height: 1;
  }
  .subheadline {
    left: 0; width: 708px; top: 322px; text-align: center; padding-left: 22px;
    color: var(--ink); font-weight: 900; font-style: italic; font-size: 46px; letter-spacing: 20px;
  }

  .promo-band {
    left: 0; top: 431px; width: 708px; height: 280px;
    background: linear-gradient(90deg, var(--band-shade) 0%, #071215 35%, var(--ink) 60%);
  }
  .promo-tab { left: 46px; top: 397px; }
  .promo-label {
    left: 48px; top: 408px; width: 430px; text-align: center;
    color: var(--paper); font-weight: 700; font-size: 42px; letter-spacing: -.5px;
  }

  .portrait {
    left: 380px; top: 448px; width: 328px; height: 352px;
    border-radius: 150px 150px 0 0;
    background: linear-gradient(180deg, #d9cbb3 0%, #e7c4ab 35%, #dcb096 70%, #c99e85 100%);
  }

  .treatments-title {
    left: 50px; top: 488px; color: var(--paper); font-weight: 700; font-size: 35px; letter-spacing: -.5px;
  }
  .treatment { left: 48px; width: 330px; color: var(--paper); }
  .treatment .num { position: absolute; left: 0; top: 0; color: var(--teal); font-weight: 700; font-size: 15px; }
  .treatment .name { margin-left: 21px; font-weight: 700; font-size: 12.5px; line-height: 16px; }
  .treatment .desc { margin-left: 21px; font-size: 9px; line-height: 11.5px; letter-spacing: -.15px; color: var(--muted-light); }

  .benefits-panel {
    left: 0; top: 711px; width: 374px; height: 272px; background: var(--paper);
    border-bottom-right-radius: 34px; z-index: 2;
  }
  .teal-base { left: 0; top: 960px; width: 708px; height: 39px; background: var(--teal); }
  .contact-panel {
    left: 374px; top: 741px; width: 334px; height: 258px; background: var(--teal);
    border-top-left-radius: 20px; z-index: 1;
  }
  .benefits-title {
    left: 0; width: 374px; top: 0; padding-top: 26px; padding-left: 12px; text-align: center;
  }
  .benefits-title h2 { color: var(--teal); font-weight: 700; font-size: 28px; letter-spacing: -.3px; }
  .benefit-list { list-style: none; position: absolute; left: 48px; top: 78px; width: 310px; }
  .benefit-list li {
    position: relative; padding-left: 24px; font-size: 13px; line-height: 16px; color: #222;
    margin-bottom: 13px;
  }
  .benefit-list svg { position: absolute; left: 0; top: 4px; }

  .hours-box {
    left: 6px; top: 5px; width: 314px; height: 90px; background: var(--paper); border-radius: 12px;
  }
  .hours-title { position: absolute; left: 0; width: 314px; top: 9px; text-align: center; color: var(--teal); font-weight: 700; font-size: 17px; }
  .hours-col { position: absolute; top: 36px; }
  .hours-col .days { font-weight: 700; font-size: 11.5px; color: var(--ink); letter-spacing: -.2px; }
  .hours-col .time { font-family: "Bebas Neue", sans-serif; font-size: 35px; line-height: 30px; color: var(--ink); }
  .hours-divider { position: absolute; left: 154px; top: 41px; width: 2px; height: 36px; background: var(--ink); }

  .contact-line { position: absolute; left: 31px; color: var(--paper); font-size: 21px; line-height: 26px; font-weight: 400; white-space: nowrap; }
  .contact-line svg { position: absolute; left: 0; top: 3px; }
  .contact-line span { margin-left: 30px; }
  .phone { position: absolute; left: 31px; top: 185px; }
  .phone-number { position: absolute; left: 40px; top: -6px; font-family: "Bebas Neue", sans-serif; font-size: 52px; line-height: 50px; color: var(--paper); white-space: nowrap; letter-spacing: -.5px; }
</style>
</head>
<body>
<main class="flyer">
  <div class="abs hex-decor" role="img" aria-label="Dezentes hellblaues Wabenmuster"></div>

  <svg class="abs dot-grid" width="50" height="76" viewBox="0 0 50 76" aria-hidden="true">
    <g fill="#111">
      <circle cx="4" cy="4" r="2.6"/><circle cx="25" cy="4" r="2.6"/><circle cx="46" cy="4" r="2.6"/>
      <circle cx="4" cy="27" r="2.6"/><circle cx="25" cy="27" r="2.6"/><circle cx="46" cy="27" r="2.6"/>
      <circle cx="4" cy="50" r="2.6"/><circle cx="25" cy="50" r="2.6"/><circle cx="46" cy="50" r="2.6"/>
      <circle cx="4" cy="72" r="2.6"/><circle cx="25" cy="72" r="2.6"/><circle cx="46" cy="72" r="2.6"/>
    </g>
  </svg>

  <svg class="abs header-tab" width="511" height="111" viewBox="0 0 511 111" aria-hidden="true">
    <path d="M0 0 H511 L470 86 Q459 111 430 111 H82 Q53 111 42 86 Z" fill="#000"/>
  </svg>
  <div class="abs brand-name">FROSTANOVA</div>

  <div class="abs opening-date">1. Januar 2024</div>
  <h1 class="abs headline">GROSSE</h1>
  <div class="abs subheadline">ERÖFFNUNG</div>

  <section class="abs promo-band"></section>
  <div class="abs portrait" role="img" aria-label="Porträtfoto einer Frau mit blonden Haaren und gepflegter Haut"></div>

  <svg class="abs promo-tab" width="434" height="72" viewBox="0 0 434 72" aria-hidden="true">
    <path d="M0 4 Q0 0 6 0 H418 Q434 0 424 14 L396 62 Q390 72 376 72 H28 Q18 72 15 62 Z" fill="var(--teal)"/>
    <path d="M6 0 H418 Q434 0 424 14 L421 18 H10 Z" fill="var(--teal-dark)" opacity=".55"/>
  </svg>
  <div class="abs promo-label">SPECIAL PROMO</div>

  <h2 class="abs treatments-title">3 Behandlungen</h2>
  <div class="abs treatment" style="top:540px">
    <span class="num">1</span>
    <p class="name">Lorem ipsum dolor sit amet,</p>
    <p class="desc">Lorem ipsum dolor sit amet, consectetur adipiscing elit, sed do eiusmod tempor incididunt ut labore et dolore magna aliqua.</p>
  </div>
  <div class="abs treatment" style="top:590px">
    <span class="num">2</span>
    <p class="name">Lorem ipsum dolor sit amet,</p>
    <p class="desc">Lorem ipsum dolor sit amet, consectetur adipiscing elit, sed do eiusmod tempor incididunt ut labore et dolore magna aliqua.</p>
  </div>
  <div class="abs treatment" style="top:641px">
    <span class="num">3</span>
    <p class="name">Lorem ipsum dolor sit amet,</p>
    <p class="desc">Lorem ipsum dolor sit amet, consectetur adipiscing elit, sed do eiusmod tempor incididunt ut labore et dolore magna aliqua.</p>
  </div>

  <div class="abs teal-base"></div>

  <section class="abs contact-panel">
    <div class="abs hours-box">
      <div class="hours-title">Öffnungszeiten:</div>
      <div class="hours-col" style="left:20px">
        <div class="days">MONDAY - FRIDAY</div>
        <div class="time">9:00 - 6:00</div>
      </div>
      <div class="hours-divider"></div>
      <div class="hours-col" style="left:170px">
        <div class="days">SATURDAY</div>
        <div class="time">11:00 - 4:00</div>
      </div>
    </div>

    <div class="contact-line" style="top:114px">
      <svg width="20" height="20" viewBox="0 0 24 24" fill="none" stroke="#fff" stroke-width="1.5" aria-hidden="true">
        <circle cx="12" cy="12" r="10"/><ellipse cx="12" cy="12" rx="4.5" ry="10"/><path d="M2 12h20M4 7h16M4 17h16"/>
      </svg>
      <span>www.frostanova.com</span>
    </div>
    <div class="contact-line" style="top:145px">
      <svg width="20" height="20" viewBox="0 0 24 24" fill="none" stroke="#fff" stroke-width="1.5" aria-hidden="true">
        <rect x="2" y="5" width="20" height="14"/><path d="M2 5l10 8 10-8M2 19l7-7M22 19l-7-7"/>
      </svg>
      <span>info@frostanova.com</span>
    </div>
    <div class="phone">
      <svg width="36" height="36" viewBox="0 0 37 37" aria-hidden="true">
        <circle cx="18.5" cy="18.5" r="18" fill="#fff"/>
        <path d="M12 10c1-1 2.5-1 3 0l2 4c.4.8 0 1.6-.6 2l-1.4 1c1 2.5 3 4.5 5.5 5.5l1-1.4c.5-.6 1.3-1 2-.6l4 2c1 .5 1 2 0 3l-1.5 1.5c-1.5 1.5-5 1-9-3s-5-7.5-3.5-9z" fill="var(--teal)"/>
      </svg>
      <div class="phone-number">123-456-7890</div>
    </div>
  </section>

  <section class="abs benefits-panel">
    <div class="abs benefits-title"><h2>Ihre Vorteile</h2></div>
    <ul class="benefit-list">
      <li><svg width="14" height="14" viewBox="0 0 16 16" fill="none" stroke="#222" stroke-width="1.4" aria-hidden="true"><path d="M13.5 8.5A5.8 5.8 0 1 1 10 2.7"/><path d="M5 7.5l2.6 2.6L14.5 3"/></svg>Lorem ipsum dolor sit amet, consectetur adipiscing elit,</li>
      <li><svg width="14" height="14" viewBox="0 0 16 16" fill="none" stroke="#222" stroke-width="1.4" aria-hidden="true"><path d="M13.5 8.5A5.8 5.8 0 1 1 10 2.7"/><path d="M5 7.5l2.6 2.6L14.5 3"/></svg>Lorem ipsum dolor sit amet, consectetur adipiscing elit,</li>
      <li><svg width="14" height="14" viewBox="0 0 16 16" fill="none" stroke="#222" stroke-width="1.4" aria-hidden="true"><path d="M13.5 8.5A5.8 5.8 0 1 1 10 2.7"/><path d="M5 7.5l2.6 2.6L14.5 3"/></svg>Lorem ipsum dolor sit amet, consectetur adipiscing elit,</li>
      <li><svg width="14" height="14" viewBox="0 0 16 16" fill="none" stroke="#222" stroke-width="1.4" aria-hidden="true"><path d="M13.5 8.5A5.8 5.8 0 1 1 10 2.7"/><path d="M5 7.5l2.6 2.6L14.5 3"/></svg>Lorem ipsum dolor sit amet, consectetur adipiscing elit,</li>
    </ul>
  </section>
</main>
</body>
</html>
```